Label design for Kombucha bottles

I'm in the process of making a new brand of Kombucha called Wren Kombucha. Looking for something minimal, but with character.
NOTE: Kombucha is not a beer, it's a fermented flavoured tea which is a healthy alternative to soft drink - and as such doesn't contain any alcohol and is sugar-free.
The label can incorporate "The Quiet Lantern" logo if you so wish (not essential), also came up with a rough idea of a firey barrel idea to get you started, but interested in any other ideas. (On second thoughts disregard this, don't put in quiet lantern logo)
Specifications wise: the label will go on the front of a 330ml beer bottle on an oval-shaped label. Would be good to have examples on a bottle to reference the size of the design. Only for a size guide see the Thalby label
Target Market(s)
Hipster crowd
Logo Text
Wren Kombucha
Logo styles of interest
Character Logo
Colors
Designer to choose colors to be used in the design.
Look and feel

```html
<!DOCTYPE html>
<html lang="en">
<head>
<meta charset="utf-8">
<title>Wren Kombucha – Bottle Label</title>
<link href="https://fonts.googleapis.com/css2?family=Rye&family=Cinzel:wght@700&family=IM+Fell+English:ital@1&family=Special+Elite&display=swap" rel="stylesheet">
<style>
  :root {
    --backdrop: #f1eee6;
    --ring-green: #3fae3a;
    --ring-green-dark: #2f8a2c;
    --label-yellow: #f4d11c;
    --label-yellow-light: #f8e44a;
    --label-lime: #c9d92a;
    --ink-brown: #5a2a12;
    --ink-olive: #4a4a12;
    --ink-dark: #2b1a0e;
    --art-green: #6c9a2e;
    --art-yellow: #e7e07a;
  }
  html, body {
    margin: 0;
    padding: 0;
    width: 939px;
    height: 1200px;
    overflow: hidden;
    background: var(--backdrop);
  }
  .label {
    display: block;
    width: 939px;
    height: 1200px;
  }
  .label__ring { fill: var(--ring-green); stroke: var(--ring-green-dark); stroke-width: 4; }
  .label__field { fill: url(#fieldGlow); stroke: var(--ink-brown); stroke-width: 3; }
  .label__tagline {
    font-family: "Cinzel", serif;
    font-weight: 700;
    font-size: 28px;
    letter-spacing: 5px;
    fill: var(--ink-olive);
  }
  .label__name {
    font-family: "Rye", serif;
    fill: var(--ink-brown);
    text-anchor: middle;
  }
  .label__name--top { font-size: 100px; letter-spacing: 4px; }
  .label__name--bottom { font-size: 78px; letter-spacing: 1px; }
  .label__note {
    font-family: "IM Fell English", serif;
    font-style: italic;
    font-size: 28px;
    fill: var(--ink-brown);
  }
  .label__claim {
    font-family: "Special Elite", monospace;
    font-size: 54px;
    fill: var(--ink-dark);
    text-anchor: middle;
    letter-spacing: 2px;
  }
  .label__dot { fill: var(--ring-green); }
</style>
</head>
<body>
<svg class="label" viewBox="0 0 939 1200" xmlns="http://www.w3.org/2000/svg" role="group" aria-label="Wren Kombucha oval bottle label">
  <defs>
    <radialGradient id="fieldGlow" cx="50%" cy="45%" r="60%">
      <stop offset="0%" stop-color="var(--label-yellow-light)"/>
      <stop offset="70%" stop-color="var(--label-yellow)"/>
      <stop offset="100%" stop-color="var(--label-lime)"/>
    </radialGradient>
    <linearGradient id="artFill" x1="0" y1="0" x2="0" y2="1">
      <stop offset="0%" stop-color="var(--art-yellow)"/>
      <stop offset="100%" stop-color="var(--art-green)"/>
    </linearGradient>
    <path id="taglineArc" d="M 190 600 A 280 410 0 0 1 750 600"/>
  </defs>

  <ellipse class="label__ring" cx="470" cy="600" rx="385" ry="510"/>
  <ellipse class="label__field" cx="470" cy="600" rx="330" ry="452"/>

  <text class="label__tagline">
    <textPath href="#taglineArc" startOffset="50%" text-anchor="middle">ALL NATURAL</textPath>
  </text>

  <circle class="label__dot" cx="560" cy="270" r="18"/>

  <text class="label__name label__name--top" x="470" y="390">WREN</text>
  <text class="label__name label__name--bottom" x="470" y="490">KOMBUCHA</text>

  <text class="label__note" x="205" y="560">Homebrewed</text>
  <text class="label__note" x="595" y="705">Net: 330 ml</text>

  <rect x="370" y="570" width="200" height="270" rx="24" fill="url(#artFill)" role="img" aria-label="Illustration of a fiery barrel"/>

  <text class="label__claim" x="470" y="930">SUGAR FREE</text>
</svg>
</body>
</html>
```